Banner Design for High End Jewelry Website

We need a banner for our website (brindlestone.com) for a sale that we will be running. The banner should be a size 1187 × 400. I have included a few pieces of jewelry to be included in the banner (do not need to use all, can use just some). The banner should say:
"Christmas is Closer Than You Think Sale!"
Shop Now

Industry/Entity Type

Jewelry

```html
<!DOCTYPE html>
<html lang="en">
<head>
<meta charset="UTF-8">
<title>Christmas is Closer Than You Think Sale</title>
<link rel="stylesheet" href="https://fonts.googleapis.com/css2?family=Great+Vibes&family=Dosis:wght@600&display=swap">
<style>
  :root {
    --canvas: #ffffff;
    --red-deep: #b8000b;
    --red-mid: #d9111a;
    --red-bright: #ee2a2e;
    --snow-light: #f1f1f1;
    --snow-shade: #a9a9a9;
    --gold-light: #e2c26a;
    --gold-deep: #c29a3e;
    --brooch-light: #c9ad6a;
    --brooch-deep: #8f8466;
    --button-red: #d51f28;
    --button-edge: #9e0f16;
    --white: #ffffff;
  }
  * { margin: 0; padding: 0; box-sizing: border-box; }
  html, body {
    width: 1200px; height: 1200px; overflow: hidden;
    background: var(--canvas);
  }
  .canvas { position: relative; width: 1200px; height: 1200px; }
  .banner {
    position: absolute; left: 61px; top: 418px;
    width: 1077px; height: 363px; overflow: hidden;
  }
  .bokeh-backdrop {
    position: absolute; inset: 0;
    background:
      radial-gradient(circle at 80% 15%, rgba(255,120,120,.35), transparent 30%),
      radial-gradient(circle at 20% 40%, rgba(255,90,90,.25), transparent 35%),
      linear-gradient(180deg, var(--red-bright), var(--red-mid) 45%, var(--red-deep));
  }
  .snow-bank {
    position: absolute; left: 0; right: 0; top: 250px; bottom: 0;
    background: radial-gradient(ellipse at 50% 30%, var(--snow-light), #d7d7d7 60%, var(--snow-shade));
  }
  .headline {
    position: absolute; left: 0; right: 0; top: 26px;
    text-align: center;
    font-family: "Great Vibes", cursive;
    font-weight: 400;
    font-size: 66px; line-height: 1.2;
    word-spacing: 8px;
    color: var(--white);
    white-space: nowrap;
  }
  .piece {
    position: absolute;
    border-radius: 6px;
    background: linear-gradient(180deg, var(--gold-light), var(--gold-deep));
  }
  .piece--gem-ring { left: 189px; top: 134px; width: 145px; height: 123px; }
  .piece--earrings { left: 353px; top: 132px; width: 159px; height: 115px; }
  .piece--scale-ring { left: 557px; top: 145px; width: 127px; height: 110px; }
  .piece--brooch { left: 726px; top: 125px; width: 173px; height: 137px;
    background: linear-gradient(180deg, var(--brooch-light), var(--brooch-deep)); }
  .shop-button {
    position: absolute; left: 428px; top: 281px;
    width: 221px; height: 64px;
    border-radius: 12px;
    background: linear-gradient(180deg, #e1313a, var(--button-red));
    box-shadow: 0 4px 0 var(--button-edge);
    font-family: "Dosis", sans-serif; font-weight: 600;
    font-size: 35px; letter-spacing: 1.5px; color: var(--white);
    display: flex; align-items: center; justify-content: center;
    text-decoration: none;
  }
</style>
</head>
<body>
<div class="canvas">
  <section class="banner">
    <div class="bokeh-backdrop" role="img" aria-label="Red festive bokeh background with falling sparkles"></div>
    <div class="snow-bank" role="img" aria-label="Bank of white snow"></div>
    <h1 class="headline">Christmas is Closer Than You Think Sale!</h1>
    <div class="piece piece--gem-ring" role="img" aria-label="Photo of a gold ring set with coloured cabochon stones"></div>
    <div class="piece piece--earrings" role="img" aria-label="Photo of a pair of gold earrings with emeralds, rubies and diamonds"></div>
    <div class="piece piece--scale-ring" role="img" aria-label="Photo of a textured gold ring with diamond accents"></div>
    <div class="piece piece--brooch" role="img" aria-label="Photo of a gold and silver floral brooch"></div>
    <a class="shop-button" href="#">SHOP NOW</a>
  </section>
</div>
</body>
</html>
```